Update shopping site

Our current shopping website is outdated and we are wanting to update our shopping site to have a fresh new look/design.

Create a Web Design (Uncoded - PSD layout only)

We want you to develop the design for 4 pages:
1) Home Page
2) Remedy Type
3) Health Condition
4) Consultations

www.fernmoorwell.com

Reason: Close to choosing design and a few missing items to be resolved.

Industry/Entity Type

Shopping

```html
<!DOCTYPE html>
<html lang="en">
<head>
<meta charset="utf-8">
<title>Fernmoor Well – Herbal Dispensary</title>
<link href="https://fonts.googleapis.com/css2?family=Mulish:wght@300;400;600;700&display=swap" rel="stylesheet">
<style>
:root{
  --green:#4aa23a;
  --green-dark:#2f7d27;
  --green-footer:#5aad3a;
  --green-footer-light:#74bd52;
  --ink:#2b2b2b;
  --muted:#7a7a7a;
  --line:#dcdcdc;
  --panel:#ededed;
  --nav-top:#4a4a4a;
  --nav-bottom:#2a2a2a;
  --dark-band:#3f3f3d;
  --white:#ffffff;
}
*{box-sizing:border-box;margin:0;padding:0}
html,body{width:1200px;height:3237px;overflow:hidden}
body{font-family:"Mulish",sans-serif;color:var(--ink);background:var(--white);position:relative}
.abs{position:absolute}
a{color:inherit;text-decoration:none}

/* header */
.header{position:absolute;left:0;top:0;width:1200px;height:133px;background:var(--white)}
.account-bar{position:absolute;left:808px;top:0;width:290px;height:40px;background:#e9e9e9;clip-path:polygon(0 0,100% 0,94% 100%,6% 100%);font-size:12px;color:#666;display:flex;align-items:center;justify-content:center;gap:10px;letter-spacing:.3px}
.brand{position:absolute;left:116px;top:22px;display:flex;align-items:center;gap:10px}
.brand-dot{width:22px;height:22px;border-radius:50%;background:var(--green)}
.brand-name{font-size:22px;font-weight:700;color:var(--green-dark)}
.search{position:absolute;left:363px;top:66px;width:396px;height:39px;border:1px solid #cfcfcf;display:flex}
.search span{flex:1;font-size:12px;color:#aaa;padding:12px 12px}
.search button{width:42px;border:0;background:var(--green);display:flex;align-items:center;justify-content:center}
.cart{position:absolute;left:947px;top:60px;display:flex;gap:14px;align-items:center}
.cart-icon{width:52px;height:52px;border-radius:50%;border:2px solid #ddd;display:flex;align-items:center;justify-content:center}
.cart-text small{display:block;color:var(--green);font-size:14px}
.cart-text strong{font-weight:400;font-size:20px;color:#333}

.nav{position:absolute;left:0;top:133px;width:1200px;height:59px;background:linear-gradient(var(--nav-top),var(--nav-bottom));display:flex;padding-left:110px}
.nav a{color:#fff;font-size:17px;font-weight:600;padding:0 20px;line-height:59px;border-right:1px solid rgba(255,255,255,.15)}
.nav a.active{background:var(--green)}

/* hero */
.hero{position:absolute;left:0;top:192px;width:1200px;height:524px;background:radial-gradient(ellipse at 30% 40%,#8a6a45 0%,#5c4a36 45%,#3b362f 100%)}
.hero h1{position:absolute;left:0;width:1200px;top:185px;text-align:center;color:#fff;font-weight:600;line-height:1.1}
.hero h1 span{display:block;font-size:35px;letter-spacing:1px}
.hero h1 strong{display:block;font-size:48px;font-weight:600}
.hero .btn{position:absolute;left:512px;top:293px;width:185px;height:43px;border:2px solid #fff;color:#fff;font-size:15px;font-weight:600;display:flex;align-items:center;justify-content:center}
.arrow{position:absolute;top:228px}

/* features circles */
.panel{position:absolute;left:0;top:716px;width:1200px;height:671px;background:var(--panel)}
.circle{position:absolute;top:665px;width:292px;height:292px;border-radius:50%;border:6px solid #fff;box-shadow:0 2px 8px rgba(0,0,0,.15);text-align:center;color:#fff;padding-top:55px}
.circle.green{background:radial-gradient(circle,#5bb03f,#2f7d27)}
.circle.dark{background:radial-gradient(circle,#5a5a5a,#333)}
.circle h3{font-size:25px;font-weight:400;margin-top:12px}
.circle p{font-size:12px;opacity:.75;width:180px;margin:6px auto 0;line-height:1.35}
.circle .pill{display:inline-block;margin-top:18px;border:2px solid #fff;border-radius:20px;padding:8px 28px;font-size:14px}

.welcome-title{position:absolute;left:123px;top:1025px;font-size:35px;font-weight:400}
.welcome-title em{font-style:normal;color:var(--green)}
.welcome-copy{position:absolute;left:123px;top:1080px;width:430px;font-size:13px;line-height:1.85;color:var(--muted)}
.welcome-copy p+p{margin-top:16px}
.outline-btn{position:absolute;left:123px;top:1277px;width:130px;height:42px;border:2px solid var(--green-dark);border-radius:21px;font-size:14px;display:flex;align-items:center;justify-content:center;color:var(--green-dark);font-weight:600}
.welcome-photo{position:absolute;left:585px;top:1020px;width:530px;height:195px;border-radius:60px 20px 60px 20px;background:radial-gradient(ellipse at 40% 55%,#c33b2e 0%,#d9a86b 35%,#e8d7bd 65%,rgba(237,237,237,0) 80%)}

/* products */
.section-title{position:absolute;left:0;width:1200px;text-align:center;font-size:32px;font-weight:400}
.products{position:absolute;left:105px;top:1510px;width:990px;height:310px;display:flex}
.product{flex:1;border-right:1px solid var(--line);text-align:center;position:relative}
.product:last-child{border-right:0}
.product-photo{width:110px;height:150px;margin:32px auto 0;background:linear-gradient(#f7f7f7,#e7e5e2)}
.product h4{font-size:16px;font-weight:400;margin-top:40px}
.product small{display:block;font-size:14px;color:#555;margin-top:2px}
.buy{display:flex;justify-content:center;align-items:center;gap:18px;margin-top:16px}
.buy b{font-size:22px;font-weight:600}
.buy span{background:var(--green);color:#fff;font-size:11px;padding:8px 22px}

/* range */
.range{position:absolute;left:0;top:1897px;width:1200px;height:436px;background:linear-gradient(#454543,#353533)}
.range h2{text-align:center;color:#fff;font-weight:400;font-size:28px;margin-top:62px}
.range-item{position:absolute;display:flex;align-items:center;gap:14px;color:#eee;font-size:14px;line-height:1.5;width:330px}
.ring{width:70px;height:70px;border-radius:50%;border:2px solid rgba(255,255,255,.7);flex:none;display:flex;align-items:center;justify-content:center}

/* events */
.events-title{position:absolute;left:115px;top:2380px;font-size:28px;font-weight:400}
.event{position:absolute;top:2443px;width:302px;height:345px;border:1px solid var(--line);background:#fff;text-align:center}
.event-photo{height:197px}
.date{display:inline-block;background:var(--green);color:#fff;font-size:13px;padding:6px 18px;margin-top:-16px;position:relative}
.event h4{font-size:18px;font-weight:400;margin-top:10px}
.event p{font-size:11px;color:#777;line-height:1.5;width:230px;margin:8px auto 0}
.event .more{display:block;color:var(--green-dark);font-size:11px;font-weight:700;margin-top:10px}

/* footer */
.footer{position:absolute;left:0;top:2870px;width:1200px;height:305px;background:var(--green-footer)}
.footer-curve{position:absolute;left:0;top:2850px}
.foot-col{position:absolute;top:2928px;color:#fff}
.foot-col h5{font-size:20px;font-weight:400;margin-bottom:14px}
.foot-col li{list-style:none;font-size:13px;line-height:30px}
.foot-col p{font-size:13px;line-height:1.6}
.foot-col .phone{font-size:18px;margin-top:14px}
.socials{display:flex;gap:6px;margin-top:12px}
.socials span{width:30px;height:30px;border-radius:50%;border:2px solid #fff}
.newsletter{display:flex;margin-top:4px}
.newsletter span{width:215px;height:38px;background:#fff;font-size:12px;color:#999;padding:12px}
.newsletter b{width:96px;height:38px;background:#2f5f27;color:#fff;font-size:13px;font-weight:400;display:flex;align-items:center;justify-content:center}
.cards{display:flex;gap:10px;margin-top:22px}
.cards span{width:44px;height:26px;background:#fff;border-radius:3px}
.bottom-bar{position:absolute;left:0;top:3175px;width:1200px;height:62px;background:var(--green-footer-light);color:#fff;font-size:12px;text-align:center;line-height:62px}
</style>
</head>
<body>

<header class="header">
  <div class="account-bar"><a>LOG IN</a>|<a>REGISTER</a>|<a>MY ACCOUNT</a></div>
  <div class="brand"><span class="brand-dot"></span><span class="brand-name">Fernmoor Well</span></div>
  <div class="search"><span>Search product here</span>
    <button aria-label="Search"><svg width="18" height="18" viewBox="0 0 18 18"><circle cx="7.5" cy="7.5" r="5.5" fill="none" stroke="#fff" stroke-width="2.2"/><line x1="11.5" y1="11.5" x2="16" y2="16" stroke="#fff" stroke-width="2.4"/></svg></button>
  </div>
  <div class="cart">
    <div class="cart-icon"><svg width="24" height="24" viewBox="0 0 24 24"><path d="M4 8h16l-2 13H6z" fill="var(--green)"/><path d="M8 8a4 4 0 0 1 8 0" fill="none" stroke="var(--green)" stroke-width="2"/></svg></div>
    <div class="cart-text"><small>My Cart</small><strong>0 items</strong></div>
  </div>
</header>

<nav class="nav">
  <a class="active">Home</a><a>Remedy Type</a><a>Health Condition</a><a>Accessories &amp; Supplies</a><a>Loyalty Program</a><a>Contact Us</a>
</nav>

<section class="hero" role="img" aria-label="Wooden spoons filled with assorted dried herbs and spices on a wooden table">
  <h1><span>HUNDREDS OF QUALITY</span><strong>HERBS AVAILABLE HERE!</strong></h1>
  <a class="btn">VIEW PRODUCT</a>
  <svg class="arrow" style="left:124px" width="20" height="36" viewBox="0 0 20 36"><path d="M17 3 3 18l14 15" fill="none" stroke="#fff" stroke-width="3"/></svg>
  <svg class="arrow" style="left:1060px" width="20" height="36" viewBox="0 0 20 36"><path d="M3 3l14 15L3 33" fill="none" stroke="#fff" stroke-width="3"/></svg>
</section>

<section class="panel"></section>

<div class="circle green" style="left:124px" role="img" aria-label="Green herbal background">
  <svg width="70" height="50" viewBox="0 0 70 50"><path d="M8 18h54a27 27 0 0 1-54 0z" fill="#fff"/><line x1="36" y1="18" x2="58" y2="2" stroke="#fff" stroke-width="5" stroke-linecap="round"/></svg>
  <h3>Remedies</h3><p>Class aptent taciti sociosqu ad litora torquent per conubia nos</p><span class="pill">Click here</span>
</div>
<div class="circle green" style="left:454px" role="img" aria-label="Green herbal background">
  <svg width="70" height="50" viewBox="0 0 70 50"><path d="M12 40h46M20 40a15 15 0 1 1 30 0M28 40a7 7 0 1 1 14 0" fill="none" stroke="#fff" stroke-width="5" stroke-linecap="round"/></svg>
  <h3>Health Conditions</h3><p>Class aptent taciti sociosqu ad litora torquent per conubia nos</p><span class="pill">Click here</span>
</div>
<div class="circle dark" style="left:784px" role="img" aria-label="Dark herbal background">
  <svg width="70" height="50" viewBox="0 0 70 50"><path d="M35 48C12 44 8 24 10 4c18 4 27 18 25 44zM35 48C58 44 62 24 60 4 42 8 33 22 35 48z" fill="#fff"/></svg>
  <h3>Herbs</h3><p>Class aptent taciti sociosqu ad litora torquent per conubia nos</p><span class="pill">Click here</span>
</div>

<h2 class="welcome-title">Welcome to <em>Fernmoor Well</em></h2>
<div class="welcome-copy">
  <p>We offer some of the best botanical health care products in our industry (we require certificate of Analysis from our suppliers to ensure the purity of our product, that it is free of pesticides, contaminants, mold, fungus and it is the right product).</p>
  <p>we have over 300 NPN (Natural Product Number) licenses approved by the Herbal Standards Board and our friendly staff is well qualified to answer most questions you may have.</p>
</div>
<a class="outline-btn">Read More</a>
<div class="welcome-photo" role="img" aria-label="Dried roots, berries and sliced herbs on wooden spoons"></div>

<h2 class="section-title" style="top:1435px">Featured Products</h2>
<svg class="abs" style="left:78px;top:1605px" width="24" height="56" viewBox="0 0 24 56"><path d="M20 2 4 28l16 26" fill="none" stroke="#bbb" stroke-width="2"/></svg>
<svg class="abs" style="left:1098px;top:1605px" width="24" height="56" viewBox="0 0 24 56"><path d="M4 2l16 26L4 54" fill="none" stroke="#bbb" stroke-width="2"/></svg>
<div class="products">
  <div class="product"><div class="product-photo" role="img" aria-label="Amber dropper bottle of herbal extract"></div><h4>Goat's Rue - Extract</h4><small>(Tincture) (Galega officinalis )</small><div class="buy"><b>$13.00</b><span>BUY NOW</span></div></div>
  <div class="product"><div class="product-photo" role="img" aria-label="Amber dropper bottle of herbal extract"></div><h4>Chasteberry / Vitex</h4><small>Extract (Tincture)</small><div class="buy"><b>$13.00</b><span>BUY NOW</span></div></div>
  <div class="product"><div class="product-photo" role="img" aria-label="Amber dropper bottle of herbal extract"></div><h4>Damiana - Extract</h4><small>(Tincture) (Turnera diffusa)</small><div class="buy"><b>$13.00</b><span>BUY NOW</span></div></div>
  <div class="product"><div class="product-photo" role="img" aria-label="Amber dropper bottle of herbal extract"></div><h4>Motherwort - Extract</h4><small>(Leonurus cardiaca )</small><div class="buy"><b>$13.00</b><span>BUY NOW</span></div></div>
</div>

<section class="range" role="img" aria-label="Dark background of dried herb sprigs">
  <h2>We Provide an Exclusive Range of</h2>
</section>
<div class="range-item" style="left:125px;top:2035px"><span class="ring"><svg width="30" height="30" viewBox="0 0 30 30"><path d="M15 3l4 8 8 1-6 6 2 9-8-5-8 5 2-9-6-6 8-1z" fill="none" stroke="#fff" stroke-width="2"/></svg></span>Over 280 Organic or Wild<br>Crafted Herbs</div>
<div class="range-item" style="left:500px;top:2035px"><span class="ring"><svg width="30" height="30" viewBox="0 0 30 30"><path d="M4 8v10l8 8M26 8v10l-8 8" fill="none" stroke="#fff" stroke-width="2"/></svg></span>Healing Creams<br>and Salves</div>
<div class="range-item" style="left:770px;top:2035px"><span class="ring"><svg width="30" height="30" viewBox="0 0 30 30"><path d="M8 14h14v12H8zM15 4c3 4 0 6 0 8" fill="none" stroke="#fff" stroke-width="2"/></svg></span>Aromatherapy - All natural<br>carrier oils and infused oils</div>
<div class="range-item" style="left:125px;top:2145px"><span class="ring"><svg width="30" height="30" viewBox="0 0 30 30"><path d="M10 4h10v4l3 4v14H7V12l3-4z" fill="none" stroke="#fff" stroke-width="2"/></svg></span>Over 200 Single Tinctures along with a<br>wide array of Combination Tinctures</div>
<div class="range-item" style="left:500px;top:2145px"><span class="ring"><svg width="30" height="30" viewBox="0 0 30 30"><path d="M15 4C10 12 8 15 8 19a7 7 0 0 0 14 0c0-4-2-7-7-15z" fill="#fff"/></svg></span>Practitioner grade<br>Essential Oils</div>
<div class="range-item" style="left:770px;top:2145px"><span class="ring"><svg width="30" height="30" viewBox="0 0 30 30"><path d="M12 3h6v5l4 4v15H8V12l4-4z" fill="#fff"/></svg></span>We also do custom formulations for<br>teas, tinctures and oil blends</div>

<h2 class="events-title">Upcoming Events</h2>
<article class="event" style="left:115px"><div class="event-photo" role="img" aria-label="Spa stones with white towels and tropical flowers" style="background:linear-gradient(135deg,#e9e4d0,#b9b48f 60%,#6f8a4a)"></div><span class="date">02 Aug 2017</span><h4>Your Blog Tittle here</h4><p>netus et malesuada fames ac turpis egestas Cras id elit integer quis urna Ut ante enim dapibus malesuada fringilla eu cond</p><a class="more">READ MORE</a></article>
<article class="event" style="left:440px"><div class="event-photo" role="img" aria-label="Jars of herbs and garlic beside a meditation chart" style="background:linear-gradient(135deg,#f1ece6,#c9a37a 55%,#8a5a35)"></div><span class="date">02 Aug 2017</span><h4>Your Blog Tittle here</h4><p>netus et malesuada fames ac turpis egestas Cras id elit integer quis urna Ut ante enim dapibus malesuada fringilla eu cond</p><a class="more">READ MORE</a></article>
<article class="event" style="left:770px"><div class="event-photo" role="img" aria-label="Market stall with bowls of dried herbs and spices" style="background:linear-gradient(135deg,#6f6a3e,#a58a55 50%,#4f5a2c)"></div><span class="date">02 Aug 2017</span><h4>Your Blog Tittle here</h4><p>netus et malesuada fames ac turpis egestas Cras id elit integer quis urna Ut ante enim dapibus malesuada fringilla eu cond</p><a class="more">READ MORE</a></article>

<svg class="footer-curve" width="1200" height="40" viewBox="0 0 1200 40"><path d="M0 40Q600 -20 1200 40z" fill="var(--green-footer)"/></svg>
<footer class="footer"></footer>
<div class="foot-col" style="left:130px"><h5>Information</h5><ul><li>About Us</li><li>Loyalty Program</li><li>Shipping Information</li><li>Consultation</li><li>Privacy Policy</li><li>Terms &amp; Conditions</li></ul></div>
<div class="foot-col" style="left:330px"><h5>Resources</h5><ul><li>Health Info</li><li>Returns Policy</li><li>My Account</li><li>Order History</li><li>Newsletter</li></ul></div>
<div class="foot-col" style="left:518px"><h5>Contact Us</h5><p>418 Willow Bend Road Suite B12<br>Ashford, PA 19320</p><p class="phone">(555) 014-2870</p><p style="margin-top:12px">info@fernmoorwell.com</p><div class="socials"><span></span><span></span><span></span><span></span></div></div>
<div class="foot-col" style="left:780px"><h5>Newsletter Sign Up</h5><div class="newsletter"><span>Email address</span><b>Subscribe</b></div><div class="cards"><span></span><span></span><span></span><span></span><span></span></div></div>
<div class="bottom-bar">© 2017 Company Name All right reserved &nbsp;Term of Use</div>

</body>
</html>
```